Business card design needed

I have started a new business called Marlow Auto Electrical, although the words Marlow Auto Electrical will be used on signage and documents I actually want to market the business as MAE. The services I offer are Mobile Auto Electrical, Automotive Air Conditioning and Test And Tag. My business will be targetting the Mining Industry, Civil, Rail, Agricultural and Workshop Testing And Tagging. My auto electrical service ranges from fault finding to new vehicle and mine compliance fit outs. I have a very strong focus on quality workmanship. I will upload the logo I have designed and want to use I am happy for the logo colour to change but the design itself must stay the same. I want the design to have a modern, eye catching, energetic feel. As I am a passionate motorsport fan I am happy for this to also influence the design. I am happy for the front of the card to have only the emblem and logo design and the back to have all the info.

Industry/Entity Type

Electrical

Contact Information for Business Card

MAE Marlow Auto Electrical, Dale Penrick, Auto Electrician, Mobile No 0417263859

Requirements
Must have
• On the business card it is mandatory that the following license numbers are shown:

MVRL38462
VDA L071348
ABN 61 839 204 518

```html
<!DOCTYPE html>
<html lang="en">
<head>
<meta charset="utf-8">
<title>Marlow Auto Electrical – Business Card</title>
<link rel="stylesheet" href="https://fonts.googleapis.com/css2?family=Crimson+Text&display=swap">
<style>
  :root {
    --bg-light: #4c4c4c;
    --bg-mid: #262626;
    --bg-dark: #0d0d0d;
    --ink: #ffffff;
    --ink-soft: #f2f2f2;
    --card-w: 1200px;
    --card-h: 691px;
  }
  * { margin: 0; padding: 0; box-sizing: border-box; }
  html, body {
    width: var(--card-w);
    height: var(--card-h);
    overflow: hidden;
    background: var(--bg-dark);
  }
  .card {
    position: relative;
    width: var(--card-w);
    height: var(--card-h);
    overflow: hidden;
    font-family: "Crimson Text", Georgia, serif;
    color: var(--ink);
  }
  .card__texture {
    position: absolute;
    inset: 0;
    background:
      radial-gradient(ellipse 70% 75% at 50% 28%, var(--bg-light) 0%, var(--bg-mid) 45%, var(--bg-dark) 100%);
  }
  .brand {
    position: absolute;
    left: 0;
    right: 0;
    top: 250px;
    text-align: center;
    font-weight: 400;
    color: var(--ink);
    line-height: 1;
  }
  .brand__mark {
    display: block;
    font-size: 170px;
    letter-spacing: 4px;
    margin-left: 4px;
  }
  .brand__name {
    display: block;
    margin-top: 22px;
    font-size: 36px;
    letter-spacing: 1px;
  }
  .details {
    position: absolute;
    top: 563px;
    font-size: 24.5px;
    line-height: 31.5px;
    color: var(--ink-soft);
    white-space: nowrap;
  }
  .details--licences { left: 310px; }
  .details--contact { left: 662px; }
  .divider {
    position: absolute;
    left: 597px;
    top: 551px;
    width: 10px;
    height: 122px;
  }
</style>
</head>
<body>
  <main class="card">
    <div class="card__texture" role="img" aria-label="Dark carbon fibre weave background"></div>

    <h1 class="brand">
      <span class="brand__mark">MAE</span>
      <span class="brand__name">Marlow Auto Electrical</span>
    </h1>

    <section class="details details--licences" aria-label="Licence numbers">
      <p>MVRL38462</p>
      <p>VDA L071348</p>
      <p>ABN 61 839 204 518</p>
    </section>

    <svg class="divider" viewBox="0 0 10 122" aria-hidden="true">
      <path d="M5 0 C6.5 30 6.5 92 5 122 C3.5 92 3.5 30 5 0 Z" fill="var(--ink)"/>
    </svg>

    <section class="details details--contact" aria-label="Contact">
      <p>MAE Marlow Auto Electrical,</p>
      <p>Dale Penrick, Auto Electrician,</p>
      <p>Mobile No 0417263859</p>
    </section>
  </main>
</body>
</html>
```